Social Media Graphics - Copperfield Loop

Create 6-7 individual social media graphics (square size) to encourage folks to join our online course, using either of the text below (only one set of text per graphic:

The Lantern Ridge Method
How to Create a 7-Figure Business From Scratch
Sign Up Today!

Or

The Lantern Ridge Method
Fast-track Your Way to a Multi-Million Business!
Sign Up Today!

For the color scheme of the graphics, use 1 or 2 colors in the color palette attached; or use any colors that look nice with their outfits; AVOID using red, white and blue altogether because it will look like an Independence Day (4th of July) graphic and we don’t want that; make sure the graphics appeal to both men and women

Make sure each graphic contains 1 of the 2 pics attached; and make sure one of the graphics is all TEXT only.

Target Market(s)

men and women looking to make more money

Industry/Entity Type

entrepreneurship

Requirements
Must have
• see the text document attached
Nice to have
• We are open to a nice color design; the color palette colors are not required, especially we don't want red, white and blue used together
Should not have
• AVOID using red, white and blue altogether because it will look like an Independence Day (4th of July) graphic and we dont want that

```html
<!DOCTYPE html>
<html lang="en">
<head>
<meta charset="utf-8">
<title>The Lantern Ridge Method – Social Graphics</title>
<link rel="stylesheet" href="https://fonts.googleapis.com/css2?family=Bebas+Neue&family=Montserrat:wght@700;800&display=swap">
<style>
  :root{
    --stage:#1e0005;
    --navy:#0d3f66;
    --royal:#0b3a94;
    --sky:#0a66a8;
    --ocean:#1a7ab8;
    --azure:#2e8fe0;
    --ice:#dff1fc;
    --crimson:#a5001a;
    --scarlet:#d5132a;
    --rose:#f3c8cf;
    --plum:#8a1a5e;
    --orchid:#c77bb0;
    --blush:#f4e3ef;
    --ink:#1d1d1d;
    --white:#ffffff;
    --display:"Bebas Neue", "Oswald", sans-serif;
    --body:"Montserrat", "Arial", sans-serif;
  }
  *{margin:0;padding:0;box-sizing:border-box}
  html,body{width:893px;height:1200px;overflow:hidden;background:var(--stage)}
  .board{position:relative;width:893px;height:1200px}
  .tile{position:absolute;width:270px;height:270px;overflow:hidden}
  .tile svg.deco{position:absolute;inset:0;width:270px;height:270px}
  .title{position:absolute;left:0;right:0;font-family:var(--display);line-height:.92;text-align:center;letter-spacing:.5px}
  .photo{position:absolute}
  .copy{position:absolute}
  .copy--sans{font-family:var(--body);font-weight:700;font-size:11.5px;line-height:1.42;letter-spacing:.4px}
  .copy--display{font-family:var(--display);line-height:1.15}
  .badge{position:absolute;border-radius:50%;display:flex;align-items:center;justify-content:center;
         font-family:var(--display);color:var(--white);text-align:center;line-height:1}
  .badge::after{content:"";position:absolute;inset:5px;border-radius:50%;border:1px dotted rgba(255,255,255,.8)}
  .badge span{display:block}

  /* tile 1 – sky blue */
  .tile--sky{left:156px;top:139px;background:linear-gradient(180deg,#8fd0f4 0%,var(--ice) 35%,#ffffff 60%)}
  .tile--sky .title{top:14px;color:var(--navy);font-size:52px}
  .tile--sky .photo{left:0;top:125px;width:145px;height:145px;background:linear-gradient(180deg,#5a3a34 0%,#e0467a 55%,#1f1f1f 100%)}
  .tile--sky .copy{left:145px;top:188px;width:125px;text-align:center;color:var(--white)}
  .tile--sky .badge{left:206px;top:116px;width:70px;height:70px;background:var(--azure);font-size:15px;
                    box-shadow:0 0 0 5px #ffffff,0 0 0 9px rgba(255,255,255,.35)}

  /* tile 2 – white & crimson */
  .tile--crimson{left:466px;top:139px;background:#ffffff}
  .tile--crimson .title{top:24px;color:var(--crimson);font-size:56px}
  .tile--crimson .copy{left:14px;top:146px;color:var(--crimson);font-size:27px;line-height:1.05}
  .tile--crimson .copy .big{font-size:30px}
  .tile--crimson .badge{left:180px;top:161px;width:72px;height:72px;background:var(--scarlet);font-size:17px;
                        box-shadow:0 0 0 8px var(--rose)}

  /* tile 3 – royal blue */
  .tile--royal{left:156px;top:444px;background:#ffffff}
  .tile--royal .title{top:14px;color:var(--royal);font-size:52px}
  .tile--royal .photo{left:130px;top:125px;width:140px;height:145px;background:linear-gradient(180deg,#4a2f2a 0%,#1c1c22 45%,#1f3f74 100%)}
  .tile--royal .copy{left:10px;top:202px;color:var(--white)}
  .tile--royal .badge{left:81px;top:122px;width:80px;height:80px;background:var(--azure);font-size:22px;
                      box-shadow:0 0 0 6px #ffffff,0 0 0 10px rgba(255,255,255,.4)}

  /* tile 4 – orchid */
  .tile--orchid{left:464px;top:444px;background:linear-gradient(180deg,var(--blush) 0%,#f7eef5 40%,#e8c7de 100%)}
  .tile--orchid .title{text-align:left;color:var(--plum);font-size:44px;top:16px;left:14px;right:16px}
  .tile--orchid .title .tail{display:block;text-align:right}
  .tile--orchid .photo{left:148px;top:100px;width:122px;height:170px;background:linear-gradient(180deg,#3b2722 0%,#e0467a 50%,#1e1e1e 100%)}
  .tile--orchid .copy{left:12px;top:152px;color:var(--ink);font-size:21px;line-height:1.32}
  .tile--orchid .badge{left:125px;top:185px;width:66px;height:66px;background:var(--plum);font-size:15px;
                       box-shadow:0 0 0 5px rgba(199,123,176,.55)}
  .tile--orchid .badge span{transform:rotate(-45deg)}

  /* tile 5 – ocean blue */
  .tile--ocean{left:161px;top:749px;background:#ffffff}
  .tile--ocean .title{top:12px;color:var(--sky);font-size:52px}
  .tile--ocean .photo{left:110px;top:108px;width:140px;height:132px;background:linear-gradient(180deg,#4a2f2a 0%,#1c1c22 50%,#1f3f74 100%)}
  .tile--ocean .copy{left:13px;top:128px;color:var(--ink);font-size:20px;line-height:1.2}
  .tile--ocean .badge{left:186px;top:197px;width:64px;height:64px;background:var(--sky);font-size:15px;
                      box-shadow:0 0 0 5px rgba(120,190,240,.6)}
  .tile--ocean .badge span{transform:rotate(-45deg)}

  /* tile 6 – scarlet */
  .tile--scarlet{left:466px;top:749px;background:radial-gradient(circle at 55% 35%,#ea2a2c 0%,#c8121c 55%,#8c0008 100%)}
  .tile--scarlet .title{top:14px;color:var(--white);font-size:56px}
  .tile--scarlet .copy{left:98px;top:152px;color:var(--white);font-size:13.5px;line-height:1.45}
  .tile--scarlet .badge{left:14px;top:180px;width:76px;height:76px;background:#ea2b35;font-size:19px;
                        box-shadow:0 0 0 6px rgba(255,255,255,.9),0 0 0 11px rgba(160,0,10,.5)}
</style>
</head>
<body>
<main class="board">

  <!-- tile 1 -->
  <section class="tile tile--sky">
    <svg class="deco" viewBox="0 0 270 270" aria-hidden="true">
      <path d="M0 200 Q130 150 270 105 L270 270 L0 270Z" fill="var(--ocean)"/>
      <path d="M0 180 Q140 130 270 90" stroke="#ffffff" stroke-width="2" fill="none" opacity=".7"/>
    </svg>
    <h2 class="title">The Lantern<br>Ridge Method</h2>
    <div class="photo" role="img" aria-label="Photo of the two course hosts, arms crossed, smiling"></div>
    <div class="badge"><span>Sign Up<br>Today!</span></div>
    <p class="copy copy--sans">FAST-TRACK<br>YOUR WAY TO A<br>MULTI-MILLION<br>BUSINESS!</p>
  </section>

  <!-- tile 2 -->
  <section class="tile tile--crimson">
    <svg class="deco" viewBox="0 0 270 270" aria-hidden="true">
      <path d="M0 235 Q120 275 270 205 L270 270 L0 270Z" fill="var(--scarlet)" opacity=".85"/>
      <path d="M0 220 Q130 260 270 200" stroke="var(--scarlet)" stroke-width="1.5" fill="none"/>
      <path d="M0 250 Q150 210 270 245" stroke="#ffffff" stroke-width="1" fill="none" opacity=".8"/>
    </svg>
    <h2 class="title">The Lantern<br>Ridge Method</h2>
    <p class="copy copy--display">HOW TO CREATE A<br>7-FIGURE BUSINESS<br><span class="big">FROM SCRATCH</span></p>
    <div class="badge"><span>Sign Up<br>Today!</span></div>
  </section>

  <!-- tile 3 -->
  <section class="tile tile--royal">
    <svg class="deco" viewBox="0 0 270 270" aria-hidden="true">
      <path d="M0 120 Q60 105 140 125 L140 270 L0 270Z" fill="var(--azure)"/>
      <path d="M0 135 Q70 120 140 140" stroke="#9fd3ff" stroke-width="3" fill="none"/>
      <path d="M0 150 Q70 135 140 155" stroke="#ffffff" stroke-width="1.5" fill="none" opacity=".7"/>
    </svg>
    <h2 class="title">The Lantern<br>Ridge Method</h2>
    <div class="photo" role="img" aria-label="Photo of the two course hosts in dark outfits"></div>
    <div class="badge"><span>Sign Up<br>Today!</span></div>
    <p class="copy copy--sans">FAST-TRACK<br>YOUR WAY TO A<br>MULTI-MILLION<br>BUSINESS!</p>
  </section>

  <!-- tile 4 -->
  <section class="tile tile--orchid">
    <svg class="deco" viewBox="0 0 270 270" aria-hidden="true">
      <path d="M0 150 Q90 95 190 115 Q240 125 270 110 L270 270 L0 270Z" fill="var(--orchid)" opacity=".45"/>
      <path d="M0 20 Q40 110 150 120" stroke="var(--plum)" stroke-width=".8" fill="none" opacity=".4"/>
    </svg>
    <h2 class="title">The Lantern<span class="tail">Ridge Method</span></h2>
    <div class="photo" role="img" aria-label="Photo of the two course hosts, arms crossed, smiling"></div>
    <p class="copy copy--display">FAST-TRACK<br>YOUR WAY TO A<br>MULTI-MILLION<br>BUSINESS!</p>
    <div class="badge"><span>Sign Up<br>Today!</span></div>
  </section>

  <!-- tile 5 -->
  <section class="tile tile--ocean">
    <svg class="deco" viewBox="0 0 270 270" aria-hidden="true">
      <path d="M0 240 Q130 215 270 150 L270 270 L0 270Z" fill="#cfe9fb"/>
      <path d="M0 255 Q140 225 270 165" stroke="var(--azure)" stroke-width="1.5" fill="none"/>
      <path d="M0 262 Q150 240 270 190" stroke="#7fc4f3" stroke-width="1" fill="none"/>
    </svg>
    <h2 class="title">The Lantern<br>Ridge Method</h2>
    <div class="photo" role="img" aria-label="Photo of the two course hosts in dark outfits"></div>
    <p class="copy copy--display">HOW TO CREATE<br>A 7-FIGURE<br>BUSINESS FROM<br>SCRATCH</p>
    <div class="badge"><span>Sign Up<br>Today!</span></div>
  </section>

  <!-- tile 6 -->
  <section class="tile tile--scarlet">
    <svg class="deco" viewBox="0 0 270 270" aria-hidden="true">
      <path d="M0 170 Q140 150 270 215" stroke="#ff6a6a" stroke-width="1" fill="none" opacity=".6"/>
      <path d="M0 185 Q150 165 270 230" stroke="#ff6a6a" stroke-width="1" fill="none" opacity=".5"/>
      <path d="M0 260 Q150 200 270 255 L270 270 L0 270Z" fill="#7a0006" opacity=".6"/>
    </svg>
    <h2 class="title">The Lantern<br>Ridge Method</h2>
    <p class="copy copy--sans">HOW TO CREATE A<br>7-FIGURE BUSINESS<br>FROM SCRATCH</p>
    <div class="badge"><span>Sign Up<br>Today!</span></div>
  </section>

</main>
</body>
</html>
```